Moving Company Website

We need a webdesign for an established moving company in the Bay Area. We have chosen a wordpress template (see attached) and would like to revamp the design to give it a touch and feel of a leading moving company.
The design should be inspired by the following companies:
http://www.brisklane.com/
http://www.pkhaulers.com/
Updates

The design should be based on the following WordPress template:

http://www.layoutvault.com/demo/35782.html

And based on the image I have attached.

We will get the template PSD after we will choose a designer.

Thanks
Trevor 

Industry/Entity Type

Moving Company

Requirements
Must have
• Request a quote form must be implemented in all pages
inner pages with destinations

```html
<!DOCTYPE html>
<html lang="en">
<head>
<meta charset="utf-8">
<title>Swiftbolt Movers</title>
<link href="https://fonts.googleapis.com/css2?family=Arimo:wght@400;700&display=swap" rel="stylesheet">
<style>
:root{
  --green:#2f9a2f;
  --green-dark:#0f7a1a;
  --text:#333;
  --muted:#555;
  --line:#d6d6d6;
  --panel:#e9e9e9;
  --band:#f4f4f4;
  --orange:#f0901a;
  --white:#fff;
  --black:#111;
}
*{margin:0;padding:0;box-sizing:border-box}
html,body{width:922px;height:1200px;overflow:hidden;background:var(--white)}
body{position:relative;font-family:"Arimo",Arial,sans-serif;color:var(--text)}
.abs{position:absolute}
ul{list-style:none}

/* header */
.site-header{left:0;top:0;width:922px;height:122px;background:linear-gradient(#fff 0,#fff 92px,#e4e4e4 122px)}
.brand{left:30px;top:40px;display:flex;align-items:center;gap:8px}
.brand-mark{width:18px;height:18px;border-radius:50%;background:var(--green-dark)}
.brand-name{font-size:19px;font-weight:700;color:var(--green-dark);line-height:1.1;width:110px}
.call{right:18px;top:24px;font-size:12px;color:var(--text)}
.call strong{font-weight:400;font-size:17px;margin-left:4px}
.rule-dotted{left:412px;top:61px;width:493px;border-top:1px dotted #888}
.main-nav{right:12px;top:82px;display:flex;font-size:12px}
.main-nav a{color:var(--text);text-decoration:none;padding:0 6px;border-left:1px solid #ccc;line-height:13px}
.main-nav a:first-child{border-left:0}

/* hero */
.hero{left:0;top:122px;width:922px;height:353px;background:linear-gradient(#fff 0,#fff 310px,#e6e6e6 353px)}
.slider{left:21px;top:136px;width:608px;height:291px;background:#d9d9d9}
.slider-shadow{left:40px;top:427px;width:575px;height:14px;border-radius:50%;background:radial-gradient(ellipse at center,rgba(0,0,0,.35),rgba(0,0,0,0) 70%)}
.slide-photo{left:30px;top:144px;width:589px;height:273px;background:linear-gradient(135deg,#ece9e3 0%,#d7bb8d 45%,#c39a62 70%,#e8e4dc 100%)}
.slide-caption{left:30px;top:380px;width:589px;height:37px;background:rgba(60,60,60,.75);color:var(--white);font-size:14.5px;line-height:37px;padding-left:16px}
.slide-arrow{width:26px;height:26px;border-radius:50%;background:#222;top:262px}
.slide-arrow svg{display:block}
.prev{left:15px}.next{left:605px}

.quote{left:643px;top:135px;width:265px;height:292px;background:var(--panel);box-shadow:1px 1px 2px rgba(0,0,0,.2)}
.quote-head{height:38px;background:var(--white);color:var(--green);font-size:14px;padding:14px 0 0 18px}
.quote-row{position:absolute;left:0;width:265px;height:22px}
.quote-row label{position:absolute;right:155px;top:5px;font-size:10px;color:var(--text);white-space:nowrap}
.quote-row span{position:absolute;left:122px;width:123px;height:22px;background:var(--white);border:1px solid #c9c9c9;border-radius:4px}
.quote-submit{left:175px;top:227px;width:72px;height:26px;border-radius:3px;background:linear-gradient(#1a9a25,#0c6e14);color:var(--white);font-size:11px;text-align:center;line-height:26px}

/* feature columns */
.feature{top:505px;width:200px}
.feature-icon{width:50px;height:40px;border-radius:4px}
.feature-title{position:absolute;left:64px;top:16px;font-size:13.5px;color:var(--green)}
.feature ul{position:absolute;top:70px;left:8px}
.feature li{font-size:10.5px;line-height:22px;padding-left:13px;position:relative;white-space:nowrap}
.feature li::before,.mgmt li::before{content:"";position:absolute;left:0;top:8px;border-left:4px solid #2a7ab0;border-top:3px solid transparent;border-bottom:3px solid transparent}
.more{display:flex;align-items:center;gap:9px;font-size:10.5px;color:var(--green)}
.more i{width:12px;height:12px;border-radius:50%;background:var(--black);position:relative}
.more i::after{content:"";position:absolute;left:5px;top:3px;border-left:3px solid #fff;border-top:3px solid transparent;border-bottom:3px solid transparent}
.feature .more{position:absolute;top:189px;left:6px}

/* welcome */
.welcome{left:0;top:744px;width:922px;height:213px;background:var(--band);border-top:1px solid var(--line);border-bottom:1px solid var(--line)}
.welcome h2{position:absolute;left:30px;top:14px;font-size:15px;font-weight:400;color:var(--text)}
.welcome h2 em{font-style:normal;color:var(--green)}
.welcome-photo{position:absolute;left:30px;top:49px;width:268px;height:144px;border:2px solid #fff;box-shadow:0 0 2px rgba(0,0,0,.3);background:linear-gradient(#b8c7b0 0,#9aa78f 45%,#6b5f4e 65%,#8a2a2a 80%,#777 100%)}
.welcome p{position:absolute;left:321px;top:48px;width:585px;font-size:12px;line-height:22.4px;color:var(--text)}
.welcome .more{position:absolute;left:834px;top:183px}

/* footer columns */
.foot-col{top:980px}
.foot-col h3{font-size:13px;font-weight:400;color:var(--text);margin-bottom:14px}
.field{width:115px;height:19px;background:#e4e4e4;font-size:9.5px;color:var(--muted);line-height:19px;padding-left:8px;margin-bottom:9px}
.btn-orange{width:60px;height:19px;margin:20px 0 0 9px;background:var(--orange);color:var(--black);font-size:9.5px;line-height:19px;padding-left:9px}
.foot-text{font-size:10px;line-height:19.5px;color:var(--text)}
.foot-col .more{margin-top:9px}
.avatar{position:absolute;left:4px;top:29px;width:65px;height:58px;background:linear-gradient(#6b7a4a,#8a6a4a)}
.mgmt li{position:relative;padding-left:16px;font-size:10px;line-height:22px}

/* bottom bar */
.bottom{left:0;top:1130px;width:922px;height:70px;background:linear-gradient(#e3e3e3,#f1f1f1);border-top:1px solid var(--line)}
.social{left:31px;top:1160px;display:flex;gap:10px}
.social span{width:20px;height:20px;border-radius:2px}
.legal{right:52px;top:1150px;font-size:10px;color:var(--black)}
.legal a{color:var(--black);text-decoration:none;padding:0 4px}
.copy{right:48px;top:1176px;font-size:10px;color:var(--black)}
</style>
</head>
<body>

<header class="abs site-header"></header>
<div class="abs brand"><span class="brand-mark"></span><span class="brand-name">SWIFTBOLT MOVERS</span></div>
<div class="abs call">CALL US : <strong>555 014 7720</strong></div>
<div class="abs rule-dotted"></div>
<nav class="abs main-nav">
  <a href="#">HOME</a><a href="#">ABOUT</a><a href="#">STORAGE</a><a href="#">SERVICES</a><a href="#">ADVISOR</a><a href="#">REVIEWS</a><a href="#">GALLERY</a><a href="#">CONTACT</a>
</nav>

<section class="abs hero"></section>
<div class="abs slider"></div>
<div class="abs slider-shadow"></div>
<div class="abs slide-photo" role="img" aria-label="Cardboard shipping boxes with foam packing inserts"></div>
<div class="abs slide-caption">Lorem ipsum dolor sit amet, consectetuer adipiscing elit. Cras elit lectus, bibendum a, vitae,</div>
<div class="abs slide-arrow prev"><svg width="26" height="26"><path d="M15 9l-4 4 4 4" stroke="#fff" stroke-width="2" fill="none"/></svg></div>
<div class="abs slide-arrow next"><svg width="26" height="26"><path d="M11 9l4 4-4 4" stroke="#fff" stroke-width="2" fill="none"/></svg></div>

<aside class="abs quote">
  <div class="quote-head">REQUEST QUOTE</div>
  <div class="quote-row" style="top:54px"><label>FIRST NAME :</label><span></span></div>
  <div class="quote-row" style="top:86px"><label>LAST NAME :</label><span></span></div>
  <div class="quote-row" style="top:119px"><label>PHONE :</label><span></span></div>
  <div class="quote-row" style="top:153px"><label>EMAIL :</label><span></span></div>
  <div class="quote-row" style="top:186px"><label>SELECTED SERVICE :</label><span></span></div>
  <div class="abs quote-submit">SUBMIT</div>
</aside>

<div class="abs feature" style="left:37px">
  <div class="feature-icon" role="img" aria-label="Moving truck icon" style="background:linear-gradient(#cfe3f5,#5b8fc0)"></div>
  <div class="feature-title">MOVING</div>
  <ul><li>LOCAL</li><li>LONG DISTANCE</li><li>INTERNATIONAL</li><li>COMMERCIAL</li><li>ELITE</li></ul>
  <div class="more"><i></i>MORE</div>
</div>
<div class="abs feature" style="left:270px">
  <div class="feature-icon" role="img" aria-label="Storage box icon" style="width:36px;background:linear-gradient(#d9a85a,#8a5a20)"></div>
  <div class="feature-title" style="left:44px">STORAGE</div>
  <ul style="left:10px"><li>PROCESS</li><li>FACILITIES</li><li>LICENSES AND CREDENTIALS</li><li>LICENSES AND CREDENTIALS</li><li>LICENSES AND CREDENTIALS</li></ul>
  <div class="more" style="left:10px;top:187px"><i></i>MORE</div>
</div>
<div class="abs feature" style="left:508px">
  <div class="feature-icon" role="img" aria-label="Tools icon" style="width:34px;background:linear-gradient(#bbb,#444)"></div>
  <div class="feature-title" style="left:38px">SERVICES</div>
  <ul style="left:8px"><li>PACKING &amp; UNPACKING</li><li>BOX DELIVERY</li><li>CARPENTRY SERVICES</li><li>PROFESSIONAL SERVICES</li><li>INSTALLATION AND IT</li></ul>
  <div class="more" style="left:11px;top:187px"><i></i>MORE</div>
</div>
<div class="abs feature" style="left:724px">
  <div class="feature-icon" role="img" aria-label="Advisor person icon" style="width:30px;background:linear-gradient(#e0b890,#888)"></div>
  <div class="feature-title" style="left:35px">ADVISOR</div>
  <ul style="left:14px"><li>MOVING FAQ</li><li>CHOOSING A MOVER</li><li>PLANNING A MOVE</li><li>HOW TO SAVE MONEY</li><li>HOW TO PACK</li></ul>
  <div class="more" style="left:17px;top:187px"><i></i>MORE</div>
</div>

<section class="abs welcome">
  <h2>WELCOME TO <em>OUR SITE</em></h2>
  <div class="welcome-photo" role="img" aria-label="Truck hauling crated freight on a flatbed trailer"></div>
  <p>Nunc varius facilisis eros. Sed erat. In in velit quis arcu ornare laoreet. Curabitur adipiscing luctus massa. Integer ut purus ac augue commodo commodo. Nunc nec mi eu justo tempor consectetuer. Etiam vitae nisl. In dignissim lacus ut ante. Cras elit lectus, bibendum a, adipiscing vitae, commodo et, dui. Lorem ipsum dolor sit amet, consectetuer adipiscing elit. Nam nibh. Nunc varius facilisis eros. Sed erat. In in velit quis arcu ornare laoreet. Curabitur adipiscing luctus massa.Lorem ipsum dolor sit amet, consectetuer adipiscing elit. Cras elit lectus, bibendum a, adipiscing vitae, commodo et, dui.</p>
  <div class="more"><i></i>MORE</div>
</section>

<div class="abs foot-col" style="left:38px">
  <h3>MY ACCOUNT</h3>
  <div class="field">Enter your mail ID</div>
  <div class="field">Password</div>
  <div class="btn-orange">Submit</div>
</div>
<div class="abs foot-col" style="left:236px;width:200px">
  <h3>ABOUT US</h3>
  <p class="foot-text">Nunc varius facilisis eros. Sed erat. In in velit quis arcu ornare laoreet. Curabitur adipiscing luctus massa. Integer ut purus ac augue commodo commodo.</p>
  <div class="more"><i></i>MORE</div>
</div>
<div class="abs foot-col" style="left:491px;width:220px;height:140px">
  <h3>TESTIMONIALS</h3>
  <div class="avatar" role="img" aria-label="Customer portrait"></div>
  <p class="foot-text" style="margin-left:82px;width:135px">Nunc varius facilisis eros. Sed erat. In in velit quis arcu ornare laoreet.</p>
  <div class="more" style="position:absolute;top:112px;left:6px"><i></i>MORE</div>
</div>
<div class="abs foot-col mgmt" style="left:751px">
  <h3>MANAGEMENT</h3>
  <ul><li>Nunc varius facilisis eros.</li><li>Nunc varius facilisis eros.</li><li>Nunc varius facilisis eros.</li><li>Nunc varius facilisis eros.</li></ul>
</div>

<footer class="abs bottom"></footer>
<div class="abs social" aria-label="Social links">
  <span style="background:#3b5998"></span><span style="background:#4cb6e0"></span><span style="background:#f07a1a"></span><span style="background:#1f75b0"></span><span style="background:#2f6fa8"></span>
</div>
<div class="abs legal"><a href="#">Privacy Policy</a>|<a href="#">Terms</a>|<a href="#">Contact</a> |<a href="#">Site Map</a></div>
<div class="abs copy">© 2012 Swiftbolt Moving and Packing, All Rights Reserved</div>

</body>
</html>
```